Design for mobile app "Morvesta tracker" (design only)

We need design for our new Android application "Morvesta tracker".

Range:
+ Design layouts for 7 pages (look at attachments) in resolution 480x800. You don`t have to do all 7 pages! You can do first (main) minimum (and the rest after contest if you win).
+ You can change place of the elements, functionality (for example: method for collecting data in forms) if this give more beautiful and unique design.
+ Adjust the colors similar to used on the [url removed, login to view] (green, orange, dark gray). But! You can decide on one dominant color (in most cases, this is indicated). You do not have to use all three, do not have to be too bright colors (do not have to be 100% color from the page), you can use pastel colors as well. All depens on you.

Not in range:
- Witouth logo. You can leave, insert white space, insert some text or simple proposal of "[url removed, login to view] tracker".
- Icons for 13 activities (it depens on you - look "[url removed, login to view]" - if You think that icons are necessary, please give some exemple at least of one or leave white space).

We need someting more beautiful and different (or better) from similar apps like:
[url removed, login to view]
[url removed, login to view] (!)

PLEASE BE CREATIVE! Feel free to re-organize or change the layout. Or, keep it in the same location and change its look. But we need someting more beautiful and different from similar apps.

ADDED [url removed, login to view]:
You can decide on one dominant color (in most cases, this is indicated). You do not have to use all three, do not have to be too bright colors (do not have to be 100% color from the page), you can use pastel colors as well. All depens on you.

ADDED [url removed, login to view]
You don`t have to do all 7 pages. You can do first (main) minimum (and the rest after contest if you win).

```html
<!DOCTYPE html>
<html lang="en">
<head>
<meta charset="utf-8">
<title>Morvesta tracker – pedometer</title>
<link rel="stylesheet" href="https://fonts.googleapis.com/css2?family=Questrial&family=Roboto:wght@900&display=swap">
<style>
  :root {
    --bg: #e6e9eb;
    --screen: #ffffff;
    --dark: #58595b;
    --dark-deep: #3c3d3f;
    --green: #8aa829;
    --green-light: #a6c23c;
    --orange: #d35a21;
    --orange-light: #e07f58;
    --ink: #333333;
    --white: #ffffff;
  }
  * { margin: 0; padding: 0; box-sizing: border-box; }
  html, body { width: 1200px; height: 2235px; overflow: hidden; }
  body { background: var(--bg); font-family: "Questrial", "Century Gothic", sans-serif; position: relative; }

  .screen { position: absolute; left: 0; top: 125px; width: 1200px; height: 1984px; background: var(--screen); overflow: hidden; }

  .app-header { position: absolute; left: 0; top: 0; width: 100%; height: 135px; background: var(--dark); display: flex; align-items: center; justify-content: center; }
  .app-name { color: var(--green-light); font-size: 84px; letter-spacing: 1px; }

  .activity-select { position: absolute; left: 57px; top: 165px; width: 1086px; height: 169px; background: var(--dark-deep); border: 5px solid #6d6e70; border-radius: 18px; display: flex; align-items: center; }
  .activity-icon { width: 105px; height: 105px; margin-left: 32px; background: var(--white); border-radius: 8px; display: flex; align-items: center; justify-content: center; }
  .activity-name { flex: 1; text-align: center; color: var(--white); font-size: 92px; margin-right: 80px; }
  .select-caret { position: absolute; right: 22px; bottom: 22px; }

  .weight-label { position: absolute; top: 445px; width: 100%; text-align: center; color: var(--orange); font-size: 54px; }
  .weight-value { position: absolute; top: 510px; width: 100%; text-align: center; color: var(--ink); font-family: "Roboto", Arial, sans-serif; font-weight: 900; font-size: 230px; line-height: 1; letter-spacing: -4px; }
  .weight-kg { position: absolute; top: 745px; width: 100%; text-align: center; color: var(--orange); font-size: 54px; }
  .progress-arc { position: absolute; left: 150px; top: 810px; }

  .stat-band { position: absolute; left: 0; width: 100%; height: 169px; background: var(--green); }
  .stat-band.first { top: 1031px; }
  .stat-band.second { top: 1237px; }
  .band-end { position: absolute; top: 0; height: 169px; }
  .band-end.left { left: 0; }
  .band-end.right { right: 0; }
  .stat { position: absolute; top: 0; height: 169px; width: 500px; text-align: center; color: var(--white); }
  .stat .label { display: block; color: #3f4a12; font-size: 58px; margin-top: 6px; }
  .stat .value { display: block; font-size: 72px; margin-top: 10px; }
  .stat.col-a { left: 60px; }
  .stat.col-b { left: 610px; }

  .play-button { position: absolute; left: 301px; top: 1494px; width: 595px; height: 206px; border-radius: 18px; overflow: hidden; background: var(--orange); box-shadow: 0 6px 10px rgba(0,0,0,.18); display: flex; align-items: center; justify-content: center; }
  .play-button::before { content: ""; position: absolute; left: 0; top: 0; width: 100%; height: 50%; background: var(--orange-light); }
  .play-button svg { position: relative; }

  .goal-bar { position: absolute; left: 0; top: 1781px; width: 100%; height: 203px; }
  .goal-labels { height: 74px; background: var(--dark); display: flex; justify-content: space-between; align-items: center; padding: 0 48px; color: var(--white); font-size: 56px; }
  .goal-track { position: relative; height: 129px; background: var(--green); }
  .goal-end { position: absolute; top: 0; height: 129px; }
  .goal-end.left { left: 0; }
  .goal-end.right { right: 0; }
  .goal-weight { position: absolute; top: 26px; color: var(--white); font-size: 66px; }
  .goal-weight.start { left: 30px; }
  .goal-weight.target { right: 30px; }
  .goal-progress { position: absolute; left: 290px; top: 32px; width: 620px; height: 64px; background: var(--white); border: 6px solid var(--green-light); border-radius: 32px; overflow: hidden; }
  .goal-progress span { display: block; width: 32%; height: 100%; background: var(--orange); }
</style>
</head>
<body>
<main class="screen">
  <header class="app-header"><span class="app-name">Morvesta tracker</span></header>

  <div class="activity-select">
    <div class="activity-icon">
      <svg width="80" height="80" viewBox="0 0 80 80" aria-hidden="true">
        <circle cx="50" cy="12" r="8" fill="#3c3d3f"/>
        <path d="M30 28 L52 26 L46 48 L60 62 M46 48 L30 52 L18 70 M52 26 L66 40 M34 28 L20 40" stroke="#3c3d3f" stroke-width="8" fill="none" stroke-linecap="round" stroke-linejoin="round"/>
      </svg>
    </div>
    <span class="activity-name">pedometer</span>
    <svg class="select-caret" width="50" height="50" viewBox="0 0 50 50" aria-hidden="true"><polygon points="50,0 50,50 0,50" fill="#8aa829"/></svg>
  </div>

  <p class="weight-label">weight dropped</p>
  <p class="weight-value">500g</p>
  <p class="weight-kg">(0,0 kg)</p>
  <svg class="progress-arc" width="900" height="140" viewBox="0 0 900 140" aria-hidden="true">
    <path d="M0 135 Q450 -60 900 135 Q450 -30 0 135 Z" fill="#8aa829"/>
    <polygon points="450,20 430,55 470,55" fill="#d35a21"/>
  </svg>

  <section class="stat-band first">
    <svg class="band-end left" width="100" height="169" viewBox="0 0 100 169" aria-hidden="true"><polygon points="0,0 100,84 0,169" fill="#d35a21"/></svg>
    <svg class="band-end right" width="100" height="169" viewBox="0 0 100 169" aria-hidden="true"><polygon points="100,0 0,84 100,169" fill="#d35a21"/></svg>
    <div class="stat col-a"><span class="label">calories</span><span class="value">0 kcal</span></div>
    <div class="stat col-b"><span class="label">steps</span><span class="value">0</span></div>
  </section>

  <section class="stat-band second">
    <svg class="band-end left" width="100" height="169" viewBox="0 0 100 169" aria-hidden="true"><polygon points="0,0 100,84 0,169" fill="#d35a21"/></svg>
    <svg class="band-end right" width="100" height="169" viewBox="0 0 100 169" aria-hidden="true"><polygon points="100,0 0,84 100,169" fill="#d35a21"/></svg>
    <div class="stat col-a"><span class="label">distance</span><span class="value">0.0km</span></div>
    <div class="stat col-b"><span class="label">time</span><span class="value">00:00:00 sek</span></div>
  </section>

  <div class="play-button" aria-label="start">
    <svg width="100" height="110" viewBox="0 0 100 110" aria-hidden="true"><polygon points="0,0 100,55 0,110" fill="#ffffff"/></svg>
  </div>

  <footer class="goal-bar">
    <div class="goal-labels"><span>start</span><span>fill data</span><span>target</span></div>
    <div class="goal-track">
      <svg class="goal-end left" width="260" height="129" viewBox="0 0 260 129" aria-hidden="true"><polygon points="0,0 215,0 260,64 215,129 0,129" fill="#d35a21"/></svg>
      <svg class="goal-end right" width="260" height="129" viewBox="0 0 260 129" aria-hidden="true"><polygon points="260,0 45,0 0,64 45,129 260,129" fill="#d35a21"/></svg>
      <span class="goal-weight start">70kg</span>
      <div class="goal-progress"><span></span></div>
      <span class="goal-weight target">65kg</span>
    </div>
  </footer>
</main>
</body>
</html>
```